Business Card template designs

We need a lot of Business card designs.
Your designs will get exposure on our newly opened business-card printing website.
We are committed to quality of paper and packages we use, so they will come up very fancy.

Here is your advantage. We will put the profile of the graphic designer on our site so that you can showcase your designs to people around the world and in Japan.

A profile is not mandatory, although we encourage graphic designers to have a profile to get continuous work in the future.
We are looking forward to having many good designs.

The right of the use of design will be owned by us.
The design may be used to the products other than
business cards.

Target Market(s)

designer,photographer,creator,artist

Industry/Entity Type

Printing

Contact Information for Business Card

The back design is important.
Please check the reference file.

Requirements
Must have
• Please include the following, required information on your business card designs.
• Name: Haruka Tanabe
• Title: Designer
• Web: https://www.korimo.co.jp/kr/
• Address: 4-17 Kitaharazono-Cho Nerima-ku, Tokyo
• Email: info@kkorimo.com
• Phone: 03 6184 3970
• Mobile: 070 4213 6087
• * For Japanese sites, we will convert the text portion to Japanese characters.
• * In case of 28mmx70mm only include Name,Enail,Phone and SNS account(https://www.facebook.com/kkorimo.com)
• 1. colorful
• 2. simple
• 3. natural
• 4. modern
• 5. cool
• 6. sporty
• Please make variations of the same image with 3-6
• different colors / patterns for one design so that
• customers can compare and choose.
• If you want to use a same picture, please make make
• copies and paste on each different types of design.
Nice to have
• You may also use, the following non-required information.
• Company Name: Korimo, Inc.
• Fax: 03-6471-2093
• Open space for company logo

```html
<!DOCTYPE html>
<html lang="en">
<head>
<meta charset="utf-8">
<title>Business Card – Haruka Tanabe</title>
<link rel="stylesheet" href="https://fonts.googleapis.com/css2?family=Marcellus&family=Nunito+Sans:wght@400;600;700&display=swap">
<style>
  :root {
    --ink: #000000;
    --berry: #861447;
    --paper: #ffffff;
    --text-light: #e6e6e6;
    --backdrop: #ece9e6;
    --rule: #6b1038;
  }
  * { box-sizing: border-box; margin: 0; padding: 0; }
  html, body { width: 1200px; height: 900px; overflow: hidden; }
  body {
    background: var(--backdrop);
    position: relative;
    font-family: "Nunito Sans", Arial, sans-serif;
  }
  .card { position: absolute; overflow: hidden; }

  /* Front */
  .card-front {
    left: 78px; top: 35px; width: 587px; height: 362px;
    background: var(--ink);
  }
  .card-front .logo-mark {
    position: absolute; left: 122px; top: 62px;
    font-family: "Marcellus", Georgia, serif;
    font-size: 54px; color: var(--berry);
    word-spacing: 18px; letter-spacing: 0.5px;
    white-space: nowrap;
  }
  .identity {
    position: absolute; right: 319px; top: 200px;
    text-align: right; color: var(--text-light);
  }
  .identity .person-name {
    font-size: 21px; font-weight: 700; color: var(--berry);
    line-height: 26px; letter-spacing: 0.3px;
  }
  .identity .person-title { font-size: 15px; line-height: 20px; margin-bottom: 8px; }
  .identity .address { font-size: 15px; line-height: 23px; }
  .divider {
    position: absolute; left: 293px; top: 206px;
    width: 1px; height: 78px; background: var(--rule);
  }
  .contact-list {
    position: absolute; left: 312px; top: 199px;
    list-style: none; color: var(--text-light);
    font-size: 15px; line-height: 22.5px;
  }
  .contact-list li { display: flex; align-items: center; gap: 10px; }
  .contact-list svg { width: 14px; height: 14px; fill: var(--berry); flex: none; }
  .card-front .accent-band {
    position: absolute; left: 0; bottom: 0; width: 100%; height: 25px;
    background: var(--berry);
  }

  /* Back */
  .card-back {
    left: 388px; top: 505px; width: 566px; height: 352px;
    background: var(--berry);
  }
  .card-back .logo-mark {
    position: absolute; left: 0; right: 0; top: 142px;
    text-align: center;
    font-family: "Marcellus", Georgia, serif;
    font-size: 50px; color: var(--paper);
    word-spacing: 18px; padding-left: 18px;
  }
</style>
</head>
<body>
  <section class="card card-front">
    <div class="logo-mark">Logo Here</div>

    <div class="identity">
      <p class="person-name">Haruka Tanabe</p>
      <p class="person-title">Designer</p>
      <p class="address">4-17 Kitaharazono-Cho<br>Nerima-ku, Tokyo</p>
    </div>

    <div class="divider"></div>

    <ul class="contact-list">
      <li>
        <svg viewBox="0 0 16 16" aria-hidden="true"><path d="M1 5c0-2 2-3 7-3s7 1 7 3v1.5h-3.5V4.8c-1-.4-6-.4-7 0v1.7H1z"/><path d="M4 7h8l2 7H2z"/><circle cx="8" cy="10.5" r="1.8" fill="#000"/></svg>
        <span>03 6184 3970</span>
      </li>
      <li>
        <svg viewBox="0 0 16 16" aria-hidden="true"><path d="M4.5 1h7a1 1 0 0 1 1 1v12a1 1 0 0 1-1 1h-7a1 1 0 0 1-1-1V2a1 1 0 0 1 1-1zm.5 2v9h6V3z"/></svg>
        <span>070 4213 6087</span>
      </li>
      <li>
        <svg viewBox="0 0 16 16" aria-hidden="true"><path d="M1 3h14v10H1z M2.5 4.5 8 9l5.5-4.5" fill-rule="evenodd"/><path d="M2.2 4.2 8 8.8l5.8-4.6" stroke="#000" stroke-width="1.2" fill="none"/></svg>
        <span>info@kkorimo.com</span>
      </li>
      <li>
        <svg viewBox="0 0 16 16" aria-hidden="true"><circle cx="8" cy="8" r="7"/><path d="M4 4.5c1.5.3 2 1.5 3.2 1.3.6 1.2-1.3 1.8-1 3.2.4 1.3-1 1.5-1.3 2.8C3.3 10.5 2.6 7 4 4.5zM9.5 3.3c1 .8 2.5.4 3.3 1.7-.4 1.3-2 .6-2.3 2 .2 1.5 1.8 1.4 2.3 2.6-.8 1.7-2.4 2.7-3.5 2.6.2-1.5 1.2-2.3.2-3.6-1.3-.6-1.5-1.8-.6-2.6.5-.9.3-1.8.6-2.7z" fill="#000"/></svg>
        <span>www.korimo.co.jp/kr/</span>
      </li>
    </ul>

    <div class="accent-band"></div>
  </section>

  <section class="card card-back">
    <div class="logo-mark">Logo Here</div>
  </section>
</body>
</html>
```